Poster Design Project

We are launching a new company Q Vyn, we sell advertising on digital signage and we are launching our company selling ads at our 2 locations, Marlow Bend Sports and Rec Club and the Tresgold Reef Sports and Rec Club. We want to advertise that we have 5 10 and 15 ad slots available and ads start from as little as $27.00 per week. We need to let people know we offer 10% discount to LWBTO members. it needs to have the following contact details to get more information, Gideon 0479352104 and gideon@qvyn.com.au. As a new launch we are offering for the first 10 customers one of 2 discounts, get 4 weeks free all you have to pay is the content creation fee ($99 for 5 second ad) or 4 weeks free and free content creation if you sign up to a 18 week contract.

Update: need the add to start wit something like this but you can be creative:

Need to get you message or brand out, Have you heard of digital sinage?
We have ads avaliable starting from $27 per week at one of our locations.

Or something like that, as i am introducing my company they dont know what i do you untill they read this poster.

Target Market(s)

Targeting small to medium buisness

Industry/Entity Type

Advertising

Requirements
Must have
• Logo

```html
<!DOCTYPE html>
<html lang="en">
<head>
<meta charset="utf-8">
<title>Q Vyn – Digital Signage Advertising</title>
<link rel="stylesheet" href="https://fonts.googleapis.com/css2?family=Archivo+Black&display=swap">
<style>
  :root {
    --ink: #111111;
    --orange: #f39325;
    --badge-blue: #5bb8ec;
    --brand-blue: #3a8fd6;
    --band-line: #a3a6a8;
    --paper: #ffffff;
    --mist: #e6e8ea;
    --leaf-tint: #dff2d2;
  }
  * { margin: 0; padding: 0; box-sizing: border-box; }
  html, body { width: 855px; height: 1200px; overflow: hidden; background: var(--paper); }
  .poster {
    position: relative;
    width: 855px;
    height: 1200px;
    overflow: hidden;
    background: linear-gradient(180deg, #f1f2f3 0%, #ffffff 30%, #ffffff 100%);
    font-family: "Archivo Black", "Arial Black", sans-serif;
    color: var(--ink);
  }
  .brand {
    position: absolute;
    top: 112px;
    left: 0;
    width: 855px;
    display: flex;
    justify-content: center;
    align-items: center;
    gap: 14px;
    padding-right: 20px;
  }
  .brand-mark { width: 52px; height: 52px; background: var(--brand-blue); }
  .brand-name { font-size: 44px; line-height: 1; color: var(--ink); }
  .block { position: absolute; left: 0; width: 820px; text-align: center; }
  .headline { top: 193px; width: 842px; font-size: 50px; line-height: 64px; }
  .slots { top: 340px; font-size: 24px; line-height: 28px; }
  .offer-title { top: 418px; width: 850px; font-size: 32px; line-height: 38px; color: var(--orange); }
  .offer-lead { top: 461px; width: 834px; font-size: 24px; line-height: 27px; }
  .offer-detail { top: 527px; font-size: 19.5px; line-height: 25px; }
  .locations { top: 629px; width: 844px; font-size: 17px; line-height: 22px; }
  .badge {
    position: absolute;
    left: 700px;
    top: 387px;
    width: 126px;
    height: 126px;
    border-radius: 50%;
    background: var(--badge-blue);
    color: var(--paper);
    display: flex;
    flex-direction: column;
    align-items: center;
    justify-content: center;
    text-align: center;
    transform: rotate(16deg);
    font-size: 15px;
    line-height: 17px;
  }
  .badge-figure { font-size: 21px; line-height: 23px; }
  .backdrop-art {
    position: absolute;
    left: 0;
    top: 700px;
    width: 855px;
    height: 338px;
    background:
      radial-gradient(ellipse 420px 150px at 330px 230px, var(--leaf-tint) 0%, rgba(223,242,210,0) 100%),
      linear-gradient(180deg, rgba(255,255,255,0) 0%, var(--mist) 100%);
  }
  .contact-band {
    position: absolute;
    left: 0;
    top: 1038px;
    width: 855px;
    height: 162px;
    background: var(--paper);
    border-top: 6px solid var(--band-line);
  }
  .contact-band p { font-size: 49px; line-height: 60px; text-align: center; width: 836px; }
  .contact-band .contact-name { margin-top: 14px; }
</style>
</head>
<body>
<main class="poster">
  <header class="brand">
    <span class="brand-mark" aria-hidden="true"></span>
    <span class="brand-name">Q Vyn</span>
  </header>

  <h1 class="block headline">Need advertising on<br>digital signage?</h1>

  <p class="block slots">We have 5, 10 and 15 ad slots available<br>starting from as little as $27.00 per week.</p>

  <h2 class="block offer-title">New launch Offers</h2>
  <p class="block offer-lead">Be one of our first 10 customers and<br>receive one of 2 discounts.</p>
  <p class="block offer-detail">4 weeks free all you have to pay is the content creation<br>fee ($99 for 5 second ad) OR 4 weeks free and free content<br>creation if you sign up to a 18 week contract.</p>

  <p class="block locations">2 locations, Marlow Bend Sports and Rec Club and<br>the Tresgold Reef Sports and Rec Club</p>

  <div class="badge">
    <span class="badge-figure">10%</span>
    <span>discount</span>
    <span>to LWBTO</span>
    <span>members</span>
  </div>

  <div class="backdrop-art" role="img" aria-label="Decorative abstract backdrop of flowing grey lines and a green sweeping curve"></div>

  <footer class="contact-band">
    <p class="contact-name">Gideon 0479352104</p>
    <p class="contact-email">gideon@qvyn.com.au</p>
  </footer>
</main>
</body>
</html>
```